Web Design Project

Company Name: Lumivale Surgery & Laser Centre

Logo & Business Card Designs:
http://brandquillhub.com/fileshare/lumivale/Lumivale_4xOptions_1.pdf
http://brandquillhub.com/fileshare/lumivale/Lumivale-logo.jpg
http://brandquillhub.com/fileshare/lumivale/Lumivale-logo.pdf

Colour scheme - As per logo above

Navigation: Top horizontal

Page structure (with drop-downs for sub-items) -
Home
The Practice
o Dr Porlethwick
o Meet the Team
Surgical
o Breast Augmentation
o Breast Reduction
o Liposuction
o Abdominoplasty (Tummy Tuck)
o Rhinoplasty (Nose Reshaping)
o Face Lift
o Neck Lift
o Foreheadplasty (Brow Lift)
o Blepharoplasty (Eyelid Surgery)
o Arm Reduction
o Thigh Lift
o Otoplasty (Ear Pin Back)
o Fat Grafting/Fat Transfer
o Skin Cancer Surgery
Non-Surgical
o Anti-wrinkle Treatment
o Laser Skin Rejuvenation
o IPL
o Cologin Induction Treatment/Skin Needling
o Skin Peels
o Platelet Rich Plasma (PRP) Injections
Medi-Spa
o Crystal Microdermabration
o Superficial Skin Peels
o Vantri Skin Rejuvenation
o Laser Hair Removal
o Medical Micro Content
o Low Intensity Laser Therapy
o Facials
o Eye Brow Therapy
o Eye Lash Tints
Shop
Bookings
o Pricing
o Financing
o Appointments
FAQ’s
Media
Contact Us

Includes 3 'Featured Boxes' on the home page for: Breast Augmentation, Non-Surgical Procedures, Dr Porlethwick

There will be a small shopping cart facility on the page, please include an icon/button for "Start Shopping"

Include an icon/button for 'Our Monthly Offer'

Include a 'search' field

Include an enquiry form the right hand panel including the following fields: Name, Email, Phone, Service Interested In (drop-down)

Please list the phone number in the top right corner of all pages - (03) 9461 2058

Footer:
Please include a Wayfind Map icon like this site - http://www.kestorfrontguards.com.au/ with the following details-
and the following contact details:
18 Wendrell Street
Brindlemoor VIC 3987
Harlowe Bay, Australia
Tel: (03) 9461 2058
Fax: (03) 9461 3307
Email: info@lumivale.com.au

Websites they like - http://www.dorvanclinic.com.au/

Some images to use from www.plintagallery.com -

stock-illustration-20603826-medicine
stock-photo-9543790-natural-beauty
stock-photo-15520861-elegant-middle-aged-woman-with-her-arms-crossed-against-white
stock-photo-17616896-cellulite-body-and-beauty
stock-photo-20015079-laughing-man
stock-photo-20552012-our-practice-is-all-about-a-patient-s-protection
stock-photo-20741901-she-s-a-positive-and-caring-representative-of-her-profession
stock-photo-20811675-natural-beauty
stock-photo-20830587-healthy-young-fitness-woman-holding-waterbottle
stock-photo-20835175-happy-mature-woman
stock-photo-20840122-portrait-of-beautiful-girl
stock-photo-20840127-close-up-of-female-face-perfect-pure-skin
stock-photo-20840129-close-up-of-female-face-pure-skin-and-freckles
stock-photo-20840159-close-up-of-beautiful-female-face-beauty-portrait
stock-photo-20840412-beautiful-woman
stock-photo-20843352-passion-for-fruits
stock-photo-20843535-slices-of-fruit
stock-photo-20844325-beautiful-woman-enjoying-in-a-sunny-autumn-day
stock-photo-20844423-beautiful-couple-enjoying-in-autumn-day
stock-photo-20844438-beautiful-couple-rides-bikes-on-a-autumn-day
stock-photo-20845420-happy-mature-woman
stock-photo-20846541-beautiful-young-women
stock-photo-20847314-pretty-young-woman-with-cute-smile
stock-photo-20850721-healthy-elastic-skin
stock-photo-20851389-back-massage-at-spa
stock-photo-20851923-young-pensive-woman
stock-photo-20852474-relaxing-massage-at-spa
stock-photo-20852553-beautiful-young-pensive-woman
stock-photo-20853691-attractive-woman-having-botox-injections-in-face

```html
<!DOCTYPE html>
<html lang="en">
<head>
<meta charset="utf-8">
<title>Lumivale Surgery &amp; Laser Centre</title>
<link rel="stylesheet" href="https://fonts.googleapis.com/css2?family=Comfortaa:wght@400;700&family=Open+Sans:wght@400;600;700&family=Ubuntu:wght@500;700&family=Arimo:wght@400;700&display=swap">
<style>
:root{
  --teal:#2f7d78;
  --teal-dark:#1f5f5b;
  --teal-light:#5fa39c;
  --teal-text:#2e7e79;
  --page:#ffffff;
  --text:#444;
  --footer:#2b2b2b;
  --footer-bottom:#1f1f1f;
  --footer-accent:#3aa7a0;
}
*{margin:0;padding:0;box-sizing:border-box}
html,body{width:1029px;height:1200px;overflow:hidden;background:#d9d9d9}
body{position:relative;font-family:"Open Sans",Arial,sans-serif;color:var(--text)}
.abs{position:absolute}
ul{list-style:none}

/* header */
.site-header{left:0;top:0;width:1029px;height:100px;background:linear-gradient(#3f8883,#2a6d68)}
.brand{left:93px;top:8px;color:#f2f7f6;font-family:"Comfortaa",sans-serif;font-weight:400;display:flex;align-items:center;gap:10px}
.brand-name{font-size:50px;letter-spacing:1px;line-height:1}
.brand-sub{font-size:13px;letter-spacing:1px;margin-top:6px}
.brand-dot{width:34px;height:34px;border-radius:50%;background:#f2f7f6;opacity:.85}
.header-phone{right:101px;top:10px;color:#fff;font-family:"Arimo",sans-serif;font-size:22px;display:flex;align-items:center;gap:6px}
.phone-icon{width:22px;height:22px;border:1.5px solid #fff;border-radius:50%;display:flex;align-items:center;justify-content:center}

/* nav */
.main-nav{left:0;top:100px;width:1029px;height:31px;background:linear-gradient(#6a6a6a,#3c3c3c 50%,#2c2c2c)}
.main-nav ul{position:absolute;left:101px;top:0;display:flex;height:31px}
.main-nav li{height:31px;line-height:31px;text-align:center;color:#fff;font-size:11px;font-weight:600;border-right:1px solid #2a2a2a;box-shadow:1px 0 0 #707070}
.main-nav li:last-child{border:none;box-shadow:none}
.main-nav li.active{background:linear-gradient(#5e9e98,#2f7671)}
.dropdown{left:346px;top:126px;width:199px;height:149px;background:rgba(232,232,232,.92);border:1px solid #bbb;box-shadow:0 3px 8px rgba(0,0,0,.3);z-index:5;padding:13px 10px 13px 12px}
.dropdown li{height:26px;line-height:20px;font-size:9px;color:#222;padding-left:22px;border-bottom:1px dotted #999;position:relative;white-space:nowrap}
.dropdown li::before{content:"";position:absolute;left:10px;top:7px;border-left:4px solid #333;border-top:3px solid transparent;border-bottom:3px solid transparent}
.dropdown li.current{background:var(--teal);color:#fff;height:20px;margin-bottom:6px}
.dropdown li.current::before{border-left-color:#fff}

/* hero */
.hero{left:87px;top:131px;width:855px;height:287px;background:linear-gradient(#fff 40%,#ececec)}
.hero-photo{left:87px;top:131px;width:371px;height:287px;background:radial-gradient(circle at 50% 45%,#d9b39a,#f4e4d8 55%,#fbf6f1)}
.hero-title{left:443px;top:168px;width:480px;font-family:"Comfortaa",sans-serif;font-weight:700;font-size:19.5px;line-height:28px;color:var(--teal-text)}
.hero-text{left:446px;top:236px;width:466px;font-size:10.5px;line-height:17px;color:#555}
.hero-links{left:494px;top:306px;font-size:10.5px;color:var(--teal-text)}
.hero-links li{height:19px}
.hero-links li::before{content:"»";color:#666;margin-right:7px}
.offer-btn{left:757px;top:360px;width:165px;height:34px;border-radius:17px;border:2px solid #9cc9c5;background:linear-gradient(#5d9d97,#24645f);color:#fff;font-family:"Comfortaa",sans-serif;font-size:14px;display:flex;align-items:center;justify-content:center;box-shadow:0 0 0 1px #2a6a65}

/* featured band */
.band{left:0;top:418px;width:1029px;height:192px}
.band-arrow{top:494px;width:0;height:0;border-top:6px solid transparent;border-bottom:6px solid transparent}
.band-arrow.prev{left:113px;border-right:7px solid #b7d8d5}
.band-arrow.next{left:906px;border-left:7px solid #fff}
.feature{width:210px;color:#fff}
.feature h2{font-family:"Comfortaa",sans-serif;font-weight:700;font-size:15.5px;margin-bottom:9px;letter-spacing:.2px}
.feature-body{display:flex;gap:13px}
.feature-img{width:81px;height:54px;flex:none;border:2px solid #fff}
.feature-body p,.feature-more{font-size:8.7px;line-height:13.7px;font-weight:600;text-align:justify}
.feature-more{margin-top:5px}
.shop-btn{display:inline-block;margin-top:7px;background:#2b2b2b;border:1px solid #ddd;color:#fff;font-size:8.5px;padding:5px 8px}
.band-divider{top:435px;width:1px;height:135px;background:rgba(255,255,255,.3)}

/* about */
.content{left:87px;top:606px;width:855px;height:322px;background:var(--page)}
.about-title{left:99px;top:647px;width:523px;height:31px;border-top:1px dotted #bbb;border-bottom:1px dotted #bbb;font-family:"Comfortaa",sans-serif;font-weight:700;font-size:15.5px;color:var(--teal-text);line-height:29px;padding-left:1px}
.about-photo{left:92px;top:703px;width:141px;height:167px;background:radial-gradient(ellipse at 50% 40%,#d2a88d,#ead3c3 55%,#fff 80%)}
.about-divider{left:252px;top:688px;width:1px;height:190px;background:#e2e2e2}
.about-text{left:260px;top:698px;width:382px;font-family:"Arimo",sans-serif;font-size:9.2px;line-height:15.5px;color:#333;text-align:justify}
.about-text strong{color:#222}
.about-list{left:273px;top:792px;font-family:"Arimo",sans-serif;font-size:9.2px;color:#444}
.about-list li{height:20.6px;padding-left:11px;position:relative}
.about-list li::before{content:"";position:absolute;left:0;top:3px;border-left:3px solid #e0a33a;border-top:3px solid transparent;border-bottom:3px solid transparent}
.content-shadow{left:110px;top:898px;width:520px;height:14px;background:radial-gradient(ellipse at 50% 0,rgba(0,0,0,.14),transparent 70%)}

/* form */
.consult{left:683px;top:655px;width:248px;height:208px;border:2px solid #eee;border-radius:8px;background:linear-gradient(#f7f7f7,#fff);box-shadow:0 1px 3px rgba(0,0,0,.12)}
.consult h3{position:absolute;left:17px;top:12px;font-family:"Comfortaa",sans-serif;font-weight:700;font-size:15.5px;color:var(--teal-text)}
.field{position:absolute;left:0;width:227px;display:flex;align-items:center;justify-content:flex-end;gap:9px;font-family:"Arimo",sans-serif;font-size:10px;color:#444}
.field span{display:block;width:149px;height:18px;border-radius:9px;background:linear-gradient(#d3d3d3,#ececec)}
.submit{position:absolute;left:106px;top:173px;width:121px;height:23px;border-radius:10px;background:linear-gradient(#6aa7a1,#2b6762)}

/* footer */
.site-footer{left:0;top:928px;width:1029px;height:219px;background:var(--footer)}
.foot-title{top:948px;font-family:"Ubuntu",sans-serif;font-weight:700;font-size:18.5px;color:#fff;letter-spacing:.5px}
.quote-mark{left:108px;top:976px;color:#fff;font-family:Georgia,serif;font-size:30px;font-style:italic;line-height:1}
.mission-text{left:130px;top:988px;width:242px;font-family:"Arimo",sans-serif;font-size:9.2px;line-height:17.2px;color:#e6e6e6;text-align:justify}
.map{left:417px;top:983px;width:205px;height:143px;background:linear-gradient(135deg,#e5e1d6,#d8d5c9 45%,#eae3bd);border:1px solid #555}
.address{left:705px;top:982px;font-family:"Arimo",sans-serif;font-weight:700;font-size:11.5px;line-height:15.5px;color:var(--footer-accent);letter-spacing:.3px;font-style:normal}
.contact-lines{left:707px;top:1032px;font-family:"Arimo",sans-serif;font-size:10px;line-height:15.6px;color:#f0f0f0;letter-spacing:.6px}
.social{left:709px;top:1104px;display:flex;gap:8px}
.social span{width:24px;height:24px;border-radius:4px;background:linear-gradient(#f4f4f4,#c9c9c9)}
.footer-bottom{left:0;top:1147px;width:1029px;height:53px;background:var(--footer-bottom);text-align:center;font-family:"Arimo",sans-serif;font-size:8.8px;color:#e0e0e0;line-height:20px;padding-top:6px}
</style>
</head>
<body>

<header class="site-header abs">
  <div class="brand abs">
    <div>
      <div class="brand-name">LUMIVALE</div>
      <div class="brand-sub">SURGERY AND LASER CENTRE</div>
    </div>
    <span class="brand-dot"></span>
  </div>
  <div class="header-phone abs">
    <span class="phone-icon"><svg width="12" height="12" viewBox="0 0 24 24"><path fill="#fff" d="M6.6 10.8a15.1 15.1 0 0 0 6.6 6.6l2.2-2.2c.3-.3.7-.4 1-.2 1.1.4 2.3.6 3.6.6.6 0 1 .4 1 1V20c0 .6-.4 1-1 1A17 17 0 0 1 3 4c0-.6.4-1 1-1h3.5c.6 0 1 .4 1 1 0 1.3.2 2.5.6 3.6.1.3 0 .7-.2 1z"/></svg></span>
    004712 3068
  </div>
</header>

<nav class="main-nav abs">
  <ul>
    <li class="active" style="width:74px">Home</li>
    <li style="width:94px">The Practice</li>
    <li style="width:78px">Surgical</li>
    <li style="width:105px">Non-Surgical</li>
    <li style="width:84px">Medi-Spa</li>
    <li style="width:70px">Shop</li>
    <li style="width:95px">Bookings</li>
    <li style="width:78px">FAQ's</li>
    <li style="width:77px">Media</li>
    <li style="width:86px">Contact Us</li>
  </ul>
</nav>

<section class="hero abs"></section>
<div class="hero-photo abs" role="img" aria-label="Photo of a woman holding orange slices"></div>
<h1 class="hero-title abs">Dr Porlethwick and his team believe in honesty and integrity in the advice we offer,</h1>
<p class="hero-text abs">Our primary concern is the welfare of our patients and the effectiveness, safety and appropriateness of the treatments we provide. This approach is supported by the systems, standards and processes we have developed.</p>
<ul class="hero-links abs">
  <li>Our Surgeon</li>
  <li>Our Team</li>
  <li>News</li>
  <li>Monthly offers</li>
</ul>
<div class="offer-btn abs">Our Monthly Offer</div>

<ul class="dropdown abs">
  <li class="current">Anti-wrinkle Treatment</li>
  <li>Laser Skin Rejuvenation</li>
  <li>IPL</li>
  <li>Skin Peels</li>
  <li>Platelet Rich Plasma (PRP) Injections</li>
</ul>

<svg class="band abs" width="1029" height="192" viewBox="0 0 1029 192" aria-hidden="true">
  <defs>
    <linearGradient id="bandFill" x1="0" y1="0" x2="1" y2="0">
      <stop offset="0" stop-color="#2c7470"/>
      <stop offset=".5" stop-color="#34817c"/>
      <stop offset="1" stop-color="#2c7470"/>
    </linearGradient>
  </defs>
  <path d="M0 0H1029V192Q514 155 0 192Z" fill="url(#bandFill)"/>
  <rect x="0" y="0" width="1029" height="2" fill="#4b9791"/>
</svg>
<span class="band-arrow prev abs"></span>
<span class="band-arrow next abs"></span>

<article class="feature abs" style="left:149px;top:430px">
  <h2>Breast Augmentation</h2>
  <div class="feature-body">
    <div class="feature-img" role="img" aria-label="Photo of a woman measuring her chest" style="background:linear-gradient(#e8e2dc,#c9a68f)"></div>
    <p>Lorem Ipsum is simply dummy text of the printing and typesetting industry.</p>
  </div>
  <p class="feature-more">Lorem Ipsum is simply dummy text of the printing and typesetting industry.</p>
  <span class="shop-btn">Start Shopping</span>
</article>
<span class="band-divider abs" style="left:370px"></span>
<article class="feature abs" style="left:388px;top:432px">
  <h2>Non-Surgical Procedures</h2>
  <div class="feature-body">
    <div class="feature-img" role="img" aria-label="Photo of a smiling young woman" style="background:linear-gradient(#f1ece4,#b48e6e)"></div>
    <p>Lorem Ipsum is simply dummy text of the printing and typesetting industry.</p>
  </div>
  <p class="feature-more">Lorem Ipsum is simply dummy text of the printing and typesetting industry.</p>
  <span class="shop-btn">Start Shopping</span>
</article>
<span class="band-divider abs" style="left:635px"></span>
<article class="feature abs" style="left:652px;top:432px">
  <h2>Dr Porlethwick</h2>
  <div class="feature-body">
    <div class="feature-img" role="img" aria-label="Portrait photo of the surgeon" style="background:linear-gradient(#9cc7c3,#6f7f86)"></div>
    <p>Lorem Ipsum is simply dummy text of the printing and typesetting industry.</p>
  </div>
  <p class="feature-more">Lorem Ipsum is simply dummy text of the printing and typesetting industry.</p>
  <span class="shop-btn">Start Shopping</span>
</article>

<section class="content abs"></section>
<h2 class="about-title abs">About Company</h2>
<div class="about-photo abs" role="img" aria-label="Portrait photo of a woman with clear skin"></div>
<span class="about-divider abs"></span>
<p class="about-text abs"><strong>Lorem Ipsum is simply dummy text of the printing and typesetting industry. Lorem Ipsum has</strong> been the industry's standard dummy text ever since the 1500s, when an unknown printer took a galley of type and scrambled it to make a type specimen book. It has survived not only five centuries, but also the leap into electronic typesetting, remaining essentially unchanged.</p>
<ul class="about-list abs">
  <li>The results are a more youthful looking</li>
  <li>That will make friends and relatives</li>
  <li>what is different; a new hairstyle,</li>
  <li>weight loss, plastic surgery?</li>
</ul>
<div class="content-shadow abs"></div>

<form class="consult abs">
  <h3>Free Consultations</h3>
  <div class="field" style="top:64px">Name:* <span></span></div>
  <div class="field" style="top:92px">Email:* <span></span></div>
  <div class="field" style="top:119px">Phone:* <span></span></div>
  <div class="field" style="top:146px">Message:* <span></span></div>
  <div class="submit"></div>
</form>

<footer class="site-footer abs"></footer>
<h3 class="foot-title abs" style="left:133px">Our Mission</h3>
<span class="quote-mark abs">&lsquo;</span>
<p class="mission-text abs">Our primary concern is the welfare of our patients and the effectiveness, safety and appropriateness of the treatments we provide. This approach is supported by the systems, standards and processes we have developed to enable us to give you the right advice, quality care and successful outcomes.</p>

<h3 class="foot-title abs" style="left:419px;top:946px">Location</h3>
<div class="map abs" role="img" aria-label="Wayfind Map showing the clinic location"></div>

<h3 class="foot-title abs" style="left:704px">Contact Us</h3>
<address class="address abs">18 Wendrell Street<br>Brindlemoor VIC 3987<br>Harlowe Bay, Australia</address>
<div class="contact-lines abs">
  Tel: (03) 9461 2058<br>
  Fax: (03) 9461 3307<br>
  Email: info@lumivale.com.au<br>
  Website: www.lumivale.com.au
</div>
<div class="social abs" aria-label="Social links">
  <span></span><span></span><span></span>
</div>

<div class="footer-bottom abs">
  &copy; Copyright 2012 Lumivale Surgery &amp; Laser Centre (use copyright symbol)<br>
  Website &amp; Search Engine Optimisation by BrandQuillHub
</div>

</body>
</html>
```